Full Page Ad

We are like looking for something modern, Rustic and unique for a full page ad that includes our logo, office locations, contact information. Please see our webpage and www.BRINKClaimsworks.com. I can send our logo as well.
Updates

Looking for something elegant but industrial, rustic and modern. Added Sunday, June 4, 2017

Industry/Entity Type

Insurance

Font styles to use
Serif

Requirements
Must have
• Contact information

```html
<!DOCTYPE html>
<html lang="en">
<head>
<meta charset="utf-8">
<title>BRINK Claimsworks – Full Page Ad</title>
<link rel="stylesheet" href="https://fonts.googleapis.com/css2?family=Archivo+Black&family=Nunito:wght@400;600;800;900&family=Quicksand:wght@500;600;700&display=swap">
<style>
  :root{
    --navy:#13233f;
    --orange:#ef5323;
    --orange-light:#f58a3a;
    --white:#ffffff;
    --ink:#1b1b1b;
  }
  *{margin:0;padding:0;box-sizing:border-box}
  html,body{width:848px;height:1200px;overflow:hidden;background:var(--white)}
  .ad{position:relative;width:848px;height:1200px;overflow:hidden;font-family:"Quicksand",sans-serif;color:var(--ink)}
  .backdrop{position:absolute;inset:0}
  .hero-photo{position:absolute;left:0;top:145px;width:848px;height:500px}
  .brand{position:absolute;left:44px;top:16px}
  .brand-name{font-family:"Archivo Black",sans-serif;font-size:100px;line-height:.9;color:var(--navy);letter-spacing:2px}
  .brand-tagline{font-family:"Quicksand",sans-serif;font-weight:600;font-size:18px;color:var(--navy);margin-top:6px;margin-left:4px;letter-spacing:.8px}
  .promise{position:absolute;left:600px;top:62px;width:260px;transform:rotate(35deg);transform-origin:center;color:var(--white);font-family:"Nunito",sans-serif;font-weight:800;font-size:22px;line-height:1.05;text-align:center}
  .headline{position:absolute;left:34px;top:250px;color:var(--white);font-family:"Nunito",sans-serif;font-weight:800;text-shadow:2px 3px 4px rgba(0,0,0,.45)}
  .headline-top{font-size:70px;line-height:1;margin-left:95px}
  .headline-main{font-size:104px;line-height:.88;letter-spacing:-1px}
  .perils{position:absolute;left:34px;top:414px;color:var(--white);font-family:"Nunito",sans-serif;font-weight:400;font-size:38px;line-height:1.1;text-shadow:2px 2px 3px rgba(0,0,0,.45)}
  .perils b{font-weight:900}
  .perils .indent{padding-left:100px}
  .snapshot{position:absolute;border:6px solid var(--white);box-shadow:2px 3px 6px rgba(0,0,0,.35)}
  .snapshot-crash{left:24px;top:688px;width:246px;height:196px;transform:rotate(-9deg);background:linear-gradient(135deg,#6e8a4a,#9aa3ad 55%,#2c3a5c)}
  .snapshot-crew{left:246px;top:724px;width:256px;height:184px;transform:rotate(4deg);background:linear-gradient(135deg,#3a2a2c,#8a4a30 55%,#c8a030)}
  .hotline{position:absolute;left:0;top:933px;width:527px;height:64px;display:flex;align-items:center;justify-content:center;color:var(--white);font-family:"Nunito",sans-serif;font-weight:900;font-size:52px;letter-spacing:.5px}
  .address{position:absolute;left:0;top:1014px;width:527px;text-align:center;color:var(--white);font-weight:600;font-size:17.5px;line-height:1.15;font-style:normal}
  .address .lines{margin-left:20px}
  .address .numbers{margin-top:13px}
  .website{position:absolute;left:32px;top:1153px;color:var(--white);font-family:"Nunito",sans-serif;font-weight:800;font-size:22px}
  .services{position:absolute;left:535px;top:668px;width:310px;text-align:center}
  .services-title{color:var(--navy);font-family:"Nunito",sans-serif;font-weight:900;font-size:33px;line-height:1.06}
  .services-copy{margin:16px auto 0;width:244px;font-size:16.5px;font-weight:500;line-height:1.45}
  .services-copy span{display:block}
  .services-copy .fill{text-align:justify;text-align-last:justify}
  .services-copy .end{text-align:center}
  .locations-title{margin-top:12px;color:var(--orange);font-family:"Nunito",sans-serif;font-weight:900;font-size:30px}
  .locations-map{position:absolute;left:530px;top:983px;width:318px;height:217px;background:linear-gradient(180deg,var(--orange-light) 0%,#f7a66a 60%,var(--white) 100%)}
</style>
</head>
<body>
<main class="ad">
  <svg class="backdrop" width="848" height="1200" viewBox="0 0 848 1200" aria-hidden="true">
    <defs>
      <linearGradient id="heroFire" x1="0" y1="0" x2="1" y2="1">
        <stop offset="0" stop-color="#b8552a"/>
        <stop offset=".45" stop-color="#e07a45"/>
        <stop offset=".75" stop-color="#c86a3e"/>
        <stop offset="1" stop-color="#6a3a22"/>
      </linearGradient>
    </defs>
    <rect x="0" y="580" width="527" height="620" fill="var(--orange)"/>
    <path d="M0 145 H848 V625 Q640 668 440 648 Q230 628 0 591 Z" fill="url(#heroFire)"/>
    <path d="M848 612 V660 Q640 672 440 652 Q230 632 0 596 V591 Q230 626 440 644 Q640 660 848 612 Z" fill="var(--navy)"/>
    <path d="M443 0 H848 V290 C760 210 560 130 443 0 Z" fill="var(--navy)"/>
    <path d="M848 270 V620 L834 622 C846 500 846 380 848 270 Z" fill="var(--navy)"/>
    <rect x="0" y="933" width="527" height="64" fill="var(--navy)"/>
    <path d="M0 1140 H318 L344 1200 H0 Z" fill="var(--navy)"/>
  </svg>

  <div class="hero-photo" role="img" aria-label="Firefighter in protective gear spraying water at a burning house"></div>

  <header class="brand">
    <div class="brand-name">BRINK</div>
    <div class="brand-tagline">BRINK REGIONAL CLAIMS SERVICES</div>
  </header>

  <div class="promise">24/7 Claim Service<br>Fast Reporting<br>Premium Quality</div>

  <h1 class="headline">
    <div class="headline-top">When It</div>
    <div class="headline-main">Happens</div>
  </h1>

  <p class="perils">
    <b>Accidents,</b> Disasters,<br>
    <span class="indent">Fire, <b>Flood,</b> Wind,</span><br>
    Property &amp; <b>Liability</b>
  </p>

  <div class="snapshot snapshot-crash" role="img" aria-label="Two cars after a rear-end collision"></div>
  <div class="snapshot snapshot-crew" role="img" aria-label="Firefighters in helmets and breathing gear"></div>

  <div class="hotline">1-800-555-0147</div>

  <address class="address">
    <div class="lines">PO Box 218<br>410 Mill Road<br>Cedar Falls, NY 12000</div>
    <div class="numbers">Phone: 518-555-0190&nbsp; Fax: 888-555-0163</div>
  </address>

  <div class="website">www.BRINKClaimsworks.com</div>

  <section class="services">
    <h2 class="services-title">Independent<br>Claim Adjusters<br>&amp; Administration</h2>
    <p class="services-copy">
      <span class="fill">Serving you from 12 locations</span>
      <span class="fill">throughout the North East,</span>
      <span class="fill">with claim staff throughout</span>
      <span class="fill">the region, BRINK has the</span>
      <span class="fill">resources to respond to your</span>
      <span class="end">adjustment needs.</span>
    </p>
    <h3 class="locations-title">Our Locations</h3>
  </section>

  <div class="locations-map" role="img" aria-label="Map of the North East region marking the 12 office locations"></div>
</main>
</body>
</html>
```